Tidewell Hypnotherapy 2017 DL Card Flyer

We would like a double sided DL Card Flyer design.

We are a professional Hypnotherapy Clinic looking for a fresh clean design.

Front of card is summary info and back of flyer is detailed text.

I have attached documents with text for the front (dl size hypno 1) and back (dl size hypno 2) of the card and an indicative style of layout.

There are logo files uploaded as well as one image file.

The colors we like are blue, white and yellow/gold.
Updates

please note: when using the 'bright steps bold change' image, please only use the top half of the image. The girl is not to be in the image, just the words and light bulb with the chalk underline. thanks.. Added Sunday, March 19, 2017

Industry/Entity Type

Health And Wellness

Requirements
Must have
• Note. I have misspelled the www.TidewellHypnotherapy.com.au (missing an 'o' in the attachments to the brief). My error. Please amend in your design submissions.

```html
<!DOCTYPE html>
<html lang="en">
<head>
<meta charset="utf-8">
<title>Tidewell Hypnotherapy DL Flyer</title>
<link href="https://fonts.googleapis.com/css2?family=Lato:wght@400;700;900&family=Pinyon+Script&display=swap" rel="stylesheet">
<style>
:root{
  --navy:#1d2a6e;
  --blue:#2a47a8;
  --blue-deep:#172364;
  --gold:#f3d54a;
  --silver:#b9bcc3;
  --white:#ffffff;
  --stage:#a9abaf;
}
*{margin:0;padding:0;box-sizing:border-box}
html,body{width:1200px;height:949px;overflow:hidden}
body{background:radial-gradient(ellipse at 50% 40%,#cfd0d3 0%,var(--stage) 80%);font-family:"Lato",sans-serif;position:relative}
.card{position:absolute;width:448px;overflow:hidden;box-shadow:0 3px 10px rgba(0,0,0,.35)}
.front{left:126px;top:34px;height:896px;background:linear-gradient(160deg,#f4f4f6 0%,#ffffff 40%,#eeeef1 70%,#ffffff 100%)}
.back{left:612px;top:32px;height:894px;background:linear-gradient(180deg,var(--blue-deep) 0%,var(--blue) 55%,#2d4db0 100%);color:var(--white)}
.layer{position:absolute;left:0;top:0}
.brand{position:absolute;display:flex;align-items:center;gap:12px}
.brand-dot{border-radius:50%;background:var(--navy);border:5px solid #5a5e6a}
.brand-name{color:var(--navy);font-weight:900;line-height:1;text-transform:uppercase}
.front .brand{left:76px;top:52px}
.front .brand-dot{width:96px;height:96px}
.front .brand-name{font-size:33px}
.front .brand-name span{display:block;font-size:15px;font-weight:400;letter-spacing:4px;margin-top:4px}
.photo{position:absolute;left:76px;top:190px;width:296px;height:296px;border-radius:50%;
  background:radial-gradient(circle at 50% 34%,#fff6b0 0%,var(--gold) 10%,#7a7440 22%,#3a3b3c 40%,#242526 100%);
  box-shadow:0 0 0 12px #d7d8dc,0 0 0 14px #8d9097}
.tagline{position:absolute;left:0;width:448px;text-align:center;color:var(--navy);white-space:nowrap}
.tagline.script{top:520px;font-family:"Pinyon Script",cursive;font-size:33px;line-height:40px}
.tagline.bold{top:560px;font-weight:700;font-size:34px;line-height:40px}
.programs-title{position:absolute;left:52px;top:614px;width:344px;height:23px;border-radius:12px;background:var(--navy);color:var(--white);font-size:15px;text-align:center;line-height:23px;white-space:nowrap}
.programs{position:absolute;left:67px;top:637px;width:314px;height:151px;border:1px solid #333;border-top:none;list-style:none;padding:6px 0 0 22px}
.programs li{font-size:16px;color:#2b2f45;height:27px;display:flex;align-items:center;gap:8px;white-space:nowrap}
.programs svg{flex:none}
.call{position:absolute;left:0;width:448px;text-align:center;color:var(--white);white-space:nowrap}
.call.phone{top:820px;font-size:22px;font-weight:700;line-height:28px}
.call.web{top:848px;font-size:13.5px;font-weight:700;line-height:18px}
.program{position:absolute;left:0;width:448px}
.pill{height:26px;background:var(--white);border-radius:0 13px 13px 0;color:var(--navy);font-weight:700;font-size:14.4px;line-height:26px;padding-left:44px;white-space:nowrap;overflow:hidden}
.body{padding:10px 48px 0 47px;font-size:11px;line-height:13.6px;text-align:justify}
.body p{margin-bottom:4px}
.divider{position:absolute;left:38px;top:718px;width:372px;height:1px;background:rgba(255,255,255,.85)}
.closing{position:absolute;left:0;top:727px;width:448px;text-align:center;font-size:14.2px;line-height:18px}
.back .brand{left:134px;top:785px}
.back .brand-dot{width:56px;height:56px;border-width:3px}
.back .brand-name{font-size:19px}
.back .brand-name span{display:block;font-size:9px;font-weight:400;letter-spacing:2.4px;margin-top:2px}
.back-web{position:absolute;left:0;top:850px;width:448px;text-align:center;color:#222;font-weight:700;font-size:13.5px}
</style>
</head>
<body>

<section class="card front">
  <svg class="layer" width="448" height="896" viewBox="0 0 448 896" aria-hidden="true">
    <path d="M0 220 Q224 160 448 190 L448 430 Q224 440 0 480 Z" fill="var(--blue)"/>
    <path d="M0 834 Q224 770 448 834 L448 896 L0 896 Z" fill="#9da0a7"/>
    <path d="M0 848 Q224 788 448 848 L448 896 L0 896 Z" fill="var(--blue)"/>
  </svg>
  <div class="brand">
    <div class="brand-dot"></div>
    <div class="brand-name">Tidewell<span>Hypnotherapy</span></div>
  </div>
  <div class="photo" role="img" aria-label="Chalkboard with a glowing light bulb and the words bright steps bold change"></div>
  <div class="tagline script">There is nothing more important</div>
  <div class="tagline bold">THAN GOOD HEALTH</div>
  <div class="programs-title">Professional Hypnosis Therapy Programs:</div>
  <ul class="programs">
    <li><svg width="14" height="12" viewBox="0 0 14 12"><path d="M1 6 L5 10 L13 1" fill="none" stroke="var(--navy)" stroke-width="2.5"/></svg>Weight Loss (Virtual Gastric Band)</li>
    <li><svg width="14" height="12" viewBox="0 0 14 12"><path d="M1 6 L5 10 L13 1" fill="none" stroke="var(--navy)" stroke-width="2.5"/></svg>Sugar Addiction</li>
    <li><svg width="14" height="12" viewBox="0 0 14 12"><path d="M1 6 L5 10 L13 1" fill="none" stroke="var(--navy)" stroke-width="2.5"/></svg>Quit Smoking</li>
    <li><svg width="14" height="12" viewBox="0 0 14 12"><path d="M1 6 L5 10 L13 1" fill="none" stroke="var(--navy)" stroke-width="2.5"/></svg>Chronic Fatigue &amp;Chronic Pain Relief</li>
    <li><svg width="14" height="12" viewBox="0 0 14 12"><path d="M1 6 L5 10 L13 1" fill="none" stroke="var(--navy)" stroke-width="2.5"/></svg>Stress Relief &amp;Deep Relaxation</li>
  </ul>
  <div class="call phone">CALL : 1300 555 018</div>
  <div class="call web">www.TidewellHypnotherapy.com.au</div>
</section>

<section class="card back">
  <div class="program" style="top:40px">
    <div class="pill" style="width:405px">WEIGHT LOSS PROGRAM (Virtual Gastric Band)</div>
    <div class="body">
      <p>Achieve long term weight loss without dieting. Whether it's losing 3kg or 30kg, we'll help you become the shape and size you want to be.</p>
      <p>Our Internationally Accredited Program is proven to be 95% effective in clinical trials.</p>
      <p>Number of Sessions: 6+</p>
    </div>
  </div>
  <div class="program" style="top:162px">
    <div class="pill" style="width:281px;padding-left:47px">SUGAR ADDICTION PROGRAM</div>
    <div class="body">
      <p>Excess sugar intake can lead to obesity, Type 2 Diabetes and tooth decay.</p>
      <p>The habit of reaching for soft drinks, chocolate, sweets, cakes and biscuits can be hard to break.</p>
      <p>By rewiring your subconscious habits, our Program puts you back in control.</p>
      <p>Number of Sessions: 3+</p>
    </div>
  </div>
  <div class="program" style="top:313px">
    <div class="pill" style="width:420px;padding-left:42px;font-size:14px">CHRONIC FATIGUE &amp; CHRONIC PAIN RELIEF PROGRAM</div>
    <div class="body">
      <p>Chronic Fatigue, Fibromyalgia and Chronic Musculoskeletal Pain are diseases of modern living.</p>
      <p>The symptoms of fatigue and pain are very real, however the cause is usually emotional, and is generally hidden beyond our conscious awareness.</p>
      <p>Our Program comprises Education and Hypnosis to help you regain your health, your self esteem, your friends and your life, all in a manageable timeframe.</p>
      <p>Number of Sessions: 6+</p>
    </div>
  </div>
  <div class="program" style="top:494px">
    <div class="pill" style="width:374px;padding-left:46px;font-size:14px">STRESS RELIEF &amp; DEEP RELAXATION PROGRAM</div>
    <div class="body">
      <p>Our Program gently uncovers the true source of your stress, and helps you reconnect to a natural inner calm. We teach you self hypnosis so that you have the tools to continue your experience.</p>
      <p>Number of Sessions: 3+</p>
    </div>
  </div>
  <div class="program" style="top:600px">
    <div class="pill" style="width:374px;padding-left:46px;font-size:14px">STRESS RELIEF &amp; DEEP RELAXATION PROGRAM</div>
    <div class="body">
      <p>The facts speak for themselves. You are 10 times more likely to quit smoking for good using hypnotherapy.</p>
      <p>Expect to be a non smoker after completing the first session of our Program. (12 Month Guarantee)</p>
      <p>Number of Sessions: 2</p>
    </div>
  </div>
  <div class="divider"></div>
  <div class="closing">All Programs include take home CD's personally recorded<br>by our therapists, using advanced hypnotic techniques.</div>
  <svg class="layer" width="448" height="894" viewBox="0 0 448 894" aria-hidden="true">
    <path d="M0 832 Q224 730 448 832 L448 894 L0 894 Z" fill="var(--white)"/>
  </svg>
  <div class="brand">
    <div class="brand-dot"></div>
    <div class="brand-name">Tidewell<span>Hypnotherapy</span></div>
  </div>
  <div class="back-web">www.TidewellHypnotherapy.com.au</div>
</section>

</body>
</html>
```